Redesign our Product Box!

We have a product box for our pet supplement we are looking to redesign. Please use the photoshop file of the current design for the logo/info/dieline and the concept picture of a bag we would like to see included in the box design.

Ideally the background will be the green with white text, but we really want it to be fun and appealing to pet owners so do not be scared to show your vision.

```html
<!DOCTYPE html>
<html lang="en">
<head>
<meta charset="utf-8">
<title>KelpKin Box Dieline</title>
<link href="https://fonts.googleapis.com/css2?family=Source+Sans+3:wght@400;600;700&family=Roboto+Condensed:wght@700&display=swap" rel="stylesheet">
<style>
  :root {
    --green: #00a54f;
    --green-deep: #008a3e;
    --white: #ffffff;
    --ink: #222222;
    --cut: #c0272d;
    --fold: #3a4fa0;
  }
  html, body { margin: 0; padding: 0; width: 1200px; height: 1200px; overflow: hidden; background: var(--white); }
  .dieline { display: block; width: 1200px; height: 1200px; }
  .panel { fill: var(--green); stroke: var(--cut); stroke-width: 0.8; }
  .fold { stroke: var(--fold); stroke-width: 0.6; fill: none; }
  .facts-sheet { fill: var(--white); }
  .copy { font-family: "Source Sans 3", sans-serif; fill: var(--white); text-anchor: middle; }
  .brand { font-family: "Source Sans 3", sans-serif; font-weight: 700; font-size: 25px; fill: var(--white); text-anchor: middle; letter-spacing: -0.5px; }
  .tagline { font-size: 14px; }
  .body-copy { font-size: 10px; }
  .subhead { font-size: 11px; font-weight: 600; }
  .print-note { font-family: "Source Sans 3", sans-serif; font-size: 26px; fill: var(--ink); }
  .facts-title { font-family: "Roboto Condensed", sans-serif; font-weight: 700; font-size: 17px; fill: var(--ink); }
  .facts-small { font-family: "Source Sans 3", sans-serif; font-size: 6px; fill: var(--ink); }
  .facts-fine { font-family: "Source Sans 3", sans-serif; font-size: 3.6px; fill: #555; }
  .distributor { font-family: "Source Sans 3", sans-serif; font-size: 9.5px; fill: #333; }
  .warning { font-family: "Source Sans 3", sans-serif; font-size: 5.4px; fill: #555; }
  .rule { stroke: var(--ink); fill: none; }
</style>
</head>
<body>
<svg class="dieline" viewBox="555 1095 815 845" xmlns="http://www.w3.org/2000/svg" preserveAspectRatio="xMidYMid meet">
  <defs>
    <linearGradient id="waveTone" x1="0" y1="0" x2="1" y2="0">
      <stop offset="0" stop-color="#00a54f"/>
      <stop offset="0.55" stop-color="#e9f5ee"/>
      <stop offset="1" stop-color="#ffffff"/>
    </linearGradient>
  </defs>

  <!-- glue flap -->
  <polygon class="panel" points="567,1340 619,1335 619,1705 567,1700"/>

  <!-- front panel + top lid + tuck -->
  <g class="front">
    <path class="panel" d="M621,1170 C621,1135 640,1107 655,1107 L790,1107 C805,1107 822,1135 822,1170 Z"/>
    <rect class="panel" x="619" y="1170" width="205" height="165"/>
    <rect class="panel" x="619" y="1335" width="205" height="370"/>
    <text class="brand" x="721" y="1248">KelpKin</text>
    <text class="brand" x="721" y="1400">KelpKin</text>
    <text class="copy tagline" x="721" y="1442">Foundational Nutrition</text>
    <text class="copy tagline" x="721" y="1461">&amp; Super-Antioxidant</text>
    <text class="copy tagline" x="721" y="1510">For Dogs &amp; Cats</text>
    <rect x="625" y="1540" width="195" height="165" fill="url(#waveTone)" role="img" aria-label="White wave decoration sweeping across the lower front"/>
    <text class="copy body-copy" x="721" y="1680">15g</text>
  </g>

  <!-- directions side panel -->
  <g class="side-directions">
    <polygon class="panel" points="826,1222 968,1222 976,1310 988,1322 988,1335 824,1335"/>
    <rect class="panel" x="824" y="1335" width="164" height="370"/>
    <polygon class="panel" points="826,1705 988,1705 988,1818 845,1818 838,1720 826,1712"/>
    <text class="copy body-copy" x="906" y="1357">
      <tspan x="906">Directions: For dogs &amp; cats</tspan>
      <tspan x="906" dy="13.5">1/16tsp once per day.</tspan>
      <tspan x="906" dy="13.5">Administer orally. To be mixed</tspan>
      <tspan x="906" dy="13.5">into food. 1/16tsp = 1/2 the</tspan>
      <tspan x="906" dy="13.5">included scoop.</tspan>
    </text>
    <line x1="850" y1="1434" x2="964" y2="1434" stroke="var(--white)" stroke-width="0.8"/>
    <text class="copy subhead" x="906" y="1448">
      <tspan x="906">Unlock Nature’s</tspan>
      <tspan x="906" dy="15">Nutrient Treasure:</tspan>
    </text>
    <text class="copy body-copy" x="906" y="1491">
      <tspan x="906">Phytoplankton is the foundation of</tspan>
      <tspan x="906" dy="13.5">life, It is the first plant in the entire</tspan>
      <tspan x="906" dy="13.5">food chain.</tspan>
      <tspan x="906" dy="27">Phytoplankton is a microscopic</tspan>
      <tspan x="906" dy="13.5">powerhouse. Your pet’s body</tspan>
      <tspan x="906" dy="13.5">absorbs billions of phytoplankton</tspan>
      <tspan x="906" dy="13.5">with every serving.</tspan>
      <tspan x="906" dy="27">Packed with the building blocks of</tspan>
      <tspan x="906" dy="13.5">life, phytoplankton addresses</tspan>
      <tspan x="906" dy="13.5">multiple aspects of your pet’s</tspan>
      <tspan x="906" dy="13.5">health in one simple supplement.</tspan>
    </text>
  </g>

  <!-- back panel with facts -->
  <g class="back">
    <text class="print-note" x="1056" y="1252">PRINT</text>
    <text class="print-note" x="1056" y="1286">SIDE</text>
    <rect class="panel" x="988" y="1335" width="207" height="370"/>
    <rect class="facts-sheet" x="993" y="1342" width="199" height="323"/>
    <rect class="rule" x="1000" y="1350" width="185" height="97" stroke-width="1"/>
    <text class="facts-title" x="1014" y="1368">Supplement Facts</text>
    <line class="rule" x1="1003" y1="1374" x2="1182" y2="1374" stroke-width="1.5"/>
    <text class="facts-small" x="1011" y="1385" font-size="5">Serving Size: 1 Scoop/Day</text>
    <text class="facts-small" x="1011" y="1391" font-size="5">Servings per Container: 30</text>
    <text class="facts-small" x="1100" y="1391" font-size="5">Amount per Serving   %DV</text>
    <line class="rule" x1="1003" y1="1398" x2="1182" y2="1398" stroke-width="2"/>
    <text class="facts-small" x="1011" y="1414">Microalgae Nannochloropsis Gaditana</text>
    <text class="facts-small" x="1139" y="1414">500mg</text>
    <text class="facts-small" x="1170" y="1414">‡</text>
    <line class="rule" x1="1003" y1="1427" x2="1182" y2="1427" stroke-width="1.5"/>
    <text class="facts-small" x="1011" y="1438" font-size="5">‡ Daily value not established.</text>
    <text class="facts-fine" x="1000" y="1455">
      <tspan x="1000">These statements have not been evaluated by the Food and Drug Administration.</tspan>
      <tspan x="1000" dy="5">This product is not intended to diagnose, treat, cure, or prevent any disease.</tspan>
      <tspan x="1000" dy="11">Store in a cool, dry place.</tspan>
    </text>
    <text class="distributor" x="1001" y="1499">
      <tspan x="1001" font-weight="600">Distributed By:</tspan>
      <tspan x="1001" dy="12">Seabloom Pet Nutrition Inc.</tspan>
      <tspan x="1001" dy="12">42 Harbour Lane,</tspan>
      <tspan x="1001" dy="12">Halifax, Nova Scotia Canada</tspan>
      <tspan x="1001" dy="12">B3H 2K9</tspan>
    </text>
    <text class="warning" x="1000" y="1559">
      <tspan x="1000">Warnings: Check with a qualified healthcare professional before</tspan>
      <tspan x="1000" dy="6">using this product if you are pregnant, breastfeeding, or taking</tspan>
      <tspan x="1000" dy="6">blood thinners. You should call your doctor for medical advice</tspan>
      <tspan x="1000" dy="6">about serious adverse events. To report a serious adverse event</tspan>
      <tspan x="1000" dy="6">or obtain product information contact: 1 800 555 0142</tspan>
    </text>
    <text class="copy body-copy" x="1091" y="1681">
      <tspan x="1091">Customer Care: 1 800 555 0142</tspan>
      <tspan x="1091" dy="13.5">seabloompet.com</tspan>
    </text>
    <rect class="panel" x="988" y="1705" width="207" height="165"/>
    <path class="panel" d="M990,1870 L1193,1870 C1193,1905 1178,1932 1160,1932 L1024,1932 C1006,1932 990,1905 990,1870 Z"/>
    <text class="copy body-copy" transform="rotate(180 1092 1848)" x="1092" y="1851" fill="#333" style="fill:#1b3d2a">Exp: 22025/03/Lot No.:12222</text>
  </g>

  <!-- story side panel -->
  <g class="side-story">
    <polygon class="panel" points="1195,1335 1195,1322 1207,1310 1215,1222 1357,1222 1357,1335"/>
    <rect class="panel" x="1195" y="1335" width="162" height="370"/>
    <polygon class="panel" points="1195,1705 1357,1705 1357,1720 1345,1732 1338,1818 1195,1818"/>
    <text class="copy body-copy" x="1276" y="1357">
      <tspan x="1276">Our premium phytoplankton</tspan>
      <tspan x="1276" dy="13.5">powder is a extraordinary</tspan>
      <tspan x="1276" dy="13.5">supplement.  It infuses your pet’s</tspan>
      <tspan x="1276" dy="13.5">body with pure, plant-based</tspan>
      <tspan x="1276" dy="13.5">nutrients and potent antioxidants.</tspan>
      <tspan x="1276" dy="27">Phytoplankton goes beyond</tspan>
      <tspan x="1276" dy="13.5">ordinary supplements; it’s a path</tspan>
      <tspan x="1276" dy="13.5">to optimal health. In just a few</tspan>
      <tspan x="1276" dy="13.5">weeks, your pet will experience a</tspan>
      <tspan x="1276" dy="13.5">feeling of calm and strength, the</tspan>
      <tspan x="1276" dy="13.5">kind of wellness our customers</tspan>
      <tspan x="1276" dy="13.5">often say they’ve been seeking.</tspan>
      <tspan x="1276" dy="27">Join those who have discovered</tspan>
      <tspan x="1276" dy="13.5">the transformative power of</tspan>
      <tspan x="1276" dy="13.5">phytoplankton. See the difference</tspan>
      <tspan x="1276" dy="13.5">for yourself and understand why</tspan>
      <tspan x="1276" dy="13.5">it’s not just a supplement, but a</tspan>
      <tspan x="1276" dy="13.5">revolution in pet health and</tspan>
      <tspan x="1276" dy="13.5">vitality.</tspan>
    </text>
  </g>

  <!-- fold lines -->
  <g>
    <line class="fold" x1="619" y1="1335" x2="1357" y2="1335"/>
    <line class="fold" x1="619" y1="1705" x2="1357" y2="1705"/>
    <line class="fold" x1="619" y1="1170" x2="824" y2="1170"/>
    <line class="fold" x1="619" y1="1335" x2="619" y2="1705"/>
    <line class="fold" x1="824" y1="1335" x2="824" y2="1705"/>
    <line class="fold" x1="988" y1="1335" x2="988" y2="1705"/>
    <line class="fold" x1="1195" y1="1335" x2="1195" y2="1705"/>
    <line class="fold" x1="990" y1="1870" x2="1193" y2="1870"/>
  </g>
</svg>
</body>
</html>
```